Business Card Design Project

We need a double-sided business card design for our e-commerce company. Be as creative as you can.

Reason: Change of logo

Target Market(s)

Business owners

Industry/Entity Type

E-Commerce

Requirements
Must have
• Name (editable)
Mobile number -editable
www.trizvo.com - MUST STAND OUT ALONE
Office address:
27 Pellow Road
#09-04 Corbell Tower
Singapore 058214

```html
<!DOCTYPE html>
<html lang="en">
<head>
<meta charset="utf-8">
<title>Trizvo Business Card</title>
<link rel="stylesheet" href="https://fonts.googleapis.com/css2?family=Arimo:wght@400;700&display=swap">
<style>
  :root {
    --backdrop: #e6e3df;
    --card-black: #141414;
    --card-dark: #1f1f1f;
    --accent-orange: #f26b1d;
    --accent-blue: #2f7fd0;
    --name-blue: #3fa2e6;
    --text-light: #e8e8e8;
    --text-muted: #a9a9a9;
  }
  * { box-sizing: border-box; margin: 0; padding: 0; }
  html, body {
    width: 1200px; height: 1200px; overflow: hidden;
    background: var(--backdrop);
    font-family: "Arimo", Arial, sans-serif;
  }
  .canvas {
    width: 1200px; height: 1200px;
    display: flex; flex-direction: column; align-items: center; justify-content: center;
    gap: 90px;
  }
  .card {
    position: relative;
    width: 880px; height: 480px;
    background: radial-gradient(ellipse at 55% 40%, var(--card-dark), var(--card-black) 75%);
    box-shadow: 0 14px 30px rgba(0,0,0,0.28);
    overflow: hidden;
  }
  .card-stripe {
    position: absolute; left: 0; right: 0; bottom: 0; height: 26px;
    display: flex;
  }
  .card-stripe .stripe-orange { flex: 0 0 72%; background: var(--accent-orange); }
  .card-stripe .stripe-blue { flex: 1; background: var(--accent-blue); }

  /* Info side */
  .brand-mark {
    position: absolute; top: 40px; right: 56px;
    font-weight: 700; font-size: 36px; letter-spacing: 1px;
    color: var(--accent-orange);
  }
  .contact-block { position: absolute; top: 52px; left: 60px; }
  .person-name { font-size: 40px; font-weight: 400; color: var(--name-blue); }
  .person-title { margin-top: 6px; font-size: 17px; color: var(--text-muted); }
  .phone-list { margin-top: 46px; list-style: none; font-size: 20px; line-height: 1.45; color: var(--text-light); }
  .phone-list .label { color: var(--accent-orange); margin-right: 6px; }
  .office-address {
    margin-top: 40px; font-style: normal;
    font-size: 20px; line-height: 1.35; color: var(--accent-orange);
  }
  .web-address {
    position: absolute; right: 56px; bottom: 62px;
    font-weight: 700; font-size: 26px; letter-spacing: 1px;
    color: var(--accent-orange);
  }

  /* Logo side */
  .card-front { display: flex; flex-direction: column; align-items: center; justify-content: center; }
  .brand-name {
    font-weight: 700; font-size: 150px; letter-spacing: 4px;
    color: var(--accent-orange);
    margin-top: -30px;
  }
  .card-front .web-address {
    position: static; margin-top: 40px; font-size: 30px;
  }
</style>
</head>
<body>
  <main class="canvas">
    <section class="card card-back" aria-label="Business card, contact side">
      <div class="brand-mark">Trizvo</div>
      <div class="contact-block">
        <h1 class="person-name">Daniel Reyes</h1>
        <p class="person-title">Founder/Owner</p>
        <ul class="phone-list">
          <li><span class="label">P:</span>013572-046180</li>
          <li><span class="label">F:</span>013572-046190</li>
        </ul>
        <address class="office-address">
          27 Pellow Road<br>
          #09-04 Corbell Tower<br>
          Singapore 058214
        </address>
      </div>
      <p class="web-address">WWW.TRIZVO.COM</p>
      <div class="card-stripe"><span class="stripe-orange"></span><span class="stripe-blue"></span></div>
    </section>

    <section class="card card-front" aria-label="Business card, brand side">
      <h2 class="brand-name">Trizvo</h2>
      <p class="web-address">WWW.TRIZVO.COM</p>
      <div class="card-stripe"><span class="stripe-orange"></span><span class="stripe-blue"></span></div>
    </section>
  </main>
</body>
</html>
```